Creat new BusinessCard for Brightfold Consulting!

Hello Creativ Designer. I need a new Businesscard for our brand new Company "Brightfold Training". We do Consulting for a better Life & Work Situation. to create Fulfillment, Sense, Motivation and healthy Work Places in Company's. So we try to create a better World and help the employee to like what they do!
So we would like to have 2 Sites on the card. On the Back we want to put this words: "The sole meaning of life, is to serve humanity" (it can be vertical oder horizontal). In the front there is the Logo (Black or White) and Adress+ and Slogan.

Slogan on the front: -Make your Business & Life to a better place-

Name: Lukas Verhoff
Titel: Founder - Visionary - Trainer
Adress: Based in Switzerland

Tel: +41 (0) 71 583 42 17
Email: hello@brightfold-training.ch
Homepage: www.brightfold-training.ch

Thanks for your inspired Ideas and your help to make the world to a better place! IT has to be ready to print and normal Size.

Target Market(s)

insurance, Bank, Telecom, industry, IT, Medical

Contact Information for Business Card

Breite: 85 mm x Höhe: 55 mm

Colors

Designer to choose colors to be used in the design.

Requirements
Nice to have
• Thanks for your Ideas so far!
• Maybe you can try/play with the colors: Purple Code #652C8F and Grey #979797 from the Zelvor Logo purple and grey (but only a soft combination, not to much)

```html
<!DOCTYPE html>
<html lang="en">
<head>
<meta charset="utf-8">
<title>Brightfold Training – Business Card</title>
<link rel="stylesheet" href="https://fonts.googleapis.com/css2?family=Questrial&family=Montserrat:ital,wght@0,600;1,600;1,700&family=Archivo+Black&display=swap">
<style>
  :root {
    --stage: #1f2327;
    --violet-deep: #4416dc;
    --violet-mid: #5a45c8;
    --violet-soft: #7d7fb2;
    --grey-blue: #8a9ba6;
    --ink-violet: #3d1fd6;
    --quote-mark: #9c82ea;
    --quote-text: #879aa3;
    --paper: #ffffff;
  }
  * { margin: 0; padding: 0; box-sizing: border-box; }
  html, body { width: 1200px; height: 1000px; overflow: hidden; }
  body { background: var(--stage); position: relative; font-family: "Questrial", sans-serif; }

  .card { position: absolute; overflow: hidden; box-shadow: 0 8px 22px rgba(0,0,0,.45); }

  /* Front side */
  .card-front {
    left: 353px; top: 111px; width: 517px; height: 333px;
    background: linear-gradient(180deg, var(--violet-deep) 0%, var(--violet-mid) 55%, var(--violet-soft) 100%);
    color: var(--paper);
  }
  .brand-dot {
    position: absolute; left: 225px; top: 100px; width: 74px; height: 74px;
    border-radius: 50%; background: var(--paper);
  }
  .brand-name {
    position: absolute; left: 0; right: 0; top: 183px; text-align: center;
    font-family: "Montserrat", sans-serif; font-weight: 600; font-size: 20px;
    letter-spacing: .5px; color: var(--paper);
  }
  .tagline-rule {
    position: absolute; left: 0; right: 0; top: 284px;
    display: flex; align-items: center; gap: 6px;
    font-family: "Montserrat", sans-serif; font-size: 8.5px; font-weight: 600; white-space: nowrap;
    color: rgba(255,255,255,.9);
  }
  .tagline-rule::before, .tagline-rule::after {
    content: ""; flex: 1; height: 1px; background: rgba(255,255,255,.6);
  }

  /* Back side */
  .card-back {
    left: 352px; top: 548px; width: 521px; height: 336px; background: var(--paper);
  }
  .brand-disc {
    position: absolute; left: -2px; top: 0; width: 234px; height: 236px; border-radius: 50%;
    background: linear-gradient(180deg, var(--violet-deep) 0%, var(--violet-mid) 50%, var(--grey-blue) 100%);
  }
  .person { position: absolute; left: 251px; top: 57px; color: var(--ink-violet); }
  .person-name { font-size: 24px; line-height: 1.1; }
  .person-role { font-size: 17px; margin-top: 5px; }
  .contact-list { position: absolute; left: 251px; top: 135px; list-style: none; color: var(--ink-violet); }
  .contact-list li { display: flex; align-items: center; height: 30.5px; font-size: 17.5px; }
  .contact-list svg { width: 17px; height: 17px; margin-right: 9px; fill: var(--ink-violet); }

  .quote-mark {
    position: absolute; font-family: "Archivo Black", sans-serif; font-size: 78px; line-height: 1;
    color: var(--quote-mark);
  }
  .quote-open { left: 20px; top: 246px; }
  .quote-close { left: 461px; top: 289px; }
  .quote-text {
    position: absolute; font-family: "Montserrat", sans-serif; font-style: italic; font-weight: 600;
    font-size: 19.5px; color: var(--quote-text);
  }
  .quote-line-1 { left: 70px; top: 267px; }
  .quote-line-2 { left: 238px; top: 291px; }
</style>
</head>
<body>
  <section class="card card-front" aria-label="Business card front">
    <div class="brand-dot"></div>
    <div class="brand-name">Brightfold Training</div>
    <p class="tagline-rule">"Make your Business &amp; Life to a better place"</p>
  </section>

  <section class="card card-back" aria-label="Business card back">
    <div class="brand-disc"></div>
    <div class="person">
      <h1 class="person-name" style="font-weight:400">Lukas Verhoff</h1>
      <p class="person-role">Founder | Visionary | Trainer</p>
    </div>
    <ul class="contact-list">
      <li>
        <svg viewBox="0 0 24 24" aria-hidden="true"><path d="M6.6 10.8a15.1 15.1 0 0 0 6.6 6.6l2.2-2.2a1 1 0 0 1 1-.25 11.4 11.4 0 0 0 3.6.57 1 1 0 0 1 1 1V20a1 1 0 0 1-1 1A17 17 0 0 1 3 4a1 1 0 0 1 1-1h3.5a1 1 0 0 1 1 1c0 1.25.2 2.45.57 3.57a1 1 0 0 1-.25 1z"/></svg>
        +41 (0) 71 583 42 17
      </li>
      <li>
        <svg viewBox="0 0 24 24" aria-hidden="true"><path d="M2 5h20v14H2z M3.5 6.5 12 13l8.5-6.5" fill="none" stroke="currentColor"/><path d="M2 5h20v2l-10 7L2 7z"/><path d="M2 8.5l10 7 10-7V19H2z"/></svg>
        hello@brightfold-training.ch
      </li>
      <li>
        <svg viewBox="0 0 24 24" aria-hidden="true" fill="none" stroke="#3d1fd6" stroke-width="1.8" style="fill:none"><circle cx="12" cy="12" r="9"/><ellipse cx="12" cy="12" rx="4" ry="9"/><path d="M3 12h18M4.5 7.5h15M4.5 16.5h15"/></svg>
        www.brightfold-training.ch
      </li>
    </ul>
    <span class="quote-mark quote-open" aria-hidden="true">“</span>
    <p class="quote-text quote-line-1">The sole meaning of life,</p>
    <p class="quote-text quote-line-2">is to serve humanity</p>
    <span class="quote-mark quote-close" aria-hidden="true">”</span>
  </section>
</body>
</html>
```